Sanding Disc Box Packaging Graphic design

We need a package design for 5" hook and loop sanding discs designed for use with random orbital sanders.

The Brand name is "BADGER BITE". Our brand stands for Quality, Strength and durability at an affordable price.
Sanding discs packaging, and tool packaging tends to be very functional and straightforward. We are looking for a package design that is creative and stands out while maintaining a serious and professional quality look. Identifying closely with our brand name is very important as well.

I've attached images of the product, and the image the branding was inspired from. A color palette based on those images would be nice but is not necessarily required. Please note however that our discs are yellow and not red.

We do not have our box template from our manufacturer yet but the dimensions of the box will be 127x127x74mm

Target Market(s)

We are aiming at a beginner to mid-level power tool user.

Industry/Entity Type

Power Tool

Font styles to use
Serif
Decorative

Colors

Designer to choose colors to be used in the design.

Requirements
Must have
• Our Brand name, Badger Bite must be on the box, preferably in a strong Bold font.
• We would also like our slogan somewhere on the box: "Designed for Strength, Built to Last"
• I've also attached an image showing the number of pieces of each grit sandpaper is in each box. We would like some similar indication on our packaging. Also an indication that these are 8 hole sanding discs is needed as well.
Nice to have
• The packaging may also be used for other sanding products such as sanding belts, sponges, etc as the line expands so versatility is a plus. A vector design is preferred.
• A space on the back of the package for a more detailed product description with a matching font would helpful. The copy hasn't been written yet but the description will around 100 words. Placeholder text would be fine.
Should not have
• Absolutely DO NOT use images from other artists within your design. If this is done you will not win this design contest. I
• Also, please do not use the attached gorilla image in your designs. We have tried to locate the copyright holder to obtain printing rights but haven't been successful.
• Also, please stay away from the aesthetic of the product "Walrus paste". For trademark purposes the design needs to be as distinct from that product logo and packaging as possible.

```html
<!DOCTYPE html>
<html lang="en">
<head>
<meta charset="utf-8">
<title>Badger Bite – 8 Hole Sanding Discs Box</title>
<link rel="stylesheet" href="https://fonts.googleapis.com/css2?family=Oswald:wght@500;600;700&display=swap">
<style>
  :root {
    --ink: #0a0a0a;
    --orange: #f4931f;
    --white: #ffffff;
    --paper: #ffffff;
  }
  * { margin: 0; padding: 0; box-sizing: border-box; }
  html, body { width: 1200px; height: 1000px; overflow: hidden; background: var(--paper); }
  .canvas { position: relative; width: 1200px; height: 1000px; font-family: "Oswald", sans-serif; }

  .panel { position: absolute; background: var(--ink); overflow: hidden; }
  .panel--front { left: 207px; top: 111px; width: 617px; height: 618px; }
  .panel--side { left: 855px; top: 111px; width: 131px; height: 618px; }
  .panel--bottom { left: 207px; top: 757px; width: 617px; height: 131px; }

  .brand-band { position: absolute; left: 0; top: 104px; width: 617px; height: 222px; }
  .mascot-art { position: absolute; background: linear-gradient(180deg, #1a1a1a, #000); border-radius: 40px 40px 6px 6px; }
  .panel--front .mascot-art { left: 52px; top: 160px; width: 140px; height: 165px; }

  .brand-name { position: absolute; color: var(--white); font-weight: 700; text-transform: uppercase; line-height: .95; white-space: nowrap; }
  .panel--front .brand-name { left: 205px; top: 120px; font-size: 92px; letter-spacing: 1px; }

  .slogan { position: absolute; left: 0; width: 617px; top: 337px; text-align: center; color: var(--white); font-weight: 600; font-size: 33px; line-height: 42px; text-transform: uppercase; }
  .product-line { position: absolute; left: 0; width: 617px; top: 427px; text-align: center; color: var(--orange); font-weight: 600; font-size: 31px; text-transform: uppercase; }

  .grit-row { position: absolute; left: 82px; top: 480px; display: flex; gap: 23px; }
  .grit { width: 96px; text-align: center; color: var(--white); }
  .grit__count { height: 14px; font-size: 9px; line-height: 14px; }
  .grit svg { display: block; margin-top: 2px; }

  .label { color: var(--orange); font-weight: 600; font-size: 19px; line-height: 25px; text-transform: uppercase; text-align: center; }

  .vertical { writing-mode: vertical-rl; transform: rotate(180deg); }
  .panel--side .label { position: absolute; left: 33px; top: 70px; height: 82px; }
  .panel--side .brand-name { color: var(--orange); font-size: 50px; line-height: 50px; left: 18px; top: 212px; height: 226px; text-align: center; }
  .panel--side .mascot-art { left: 12px; top: 446px; width: 110px; height: 92px; background: var(--orange); opacity: .85; border-radius: 30px 40px 10px 10px; }

  .panel--bottom .mascot-art { left: 82px; top: 12px; width: 92px; height: 112px; background: var(--orange); opacity: .85; }
  .panel--bottom .brand-name { color: var(--orange); font-size: 46px; left: 210px; top: 22px; line-height: 44px; }
  .panel--bottom .label { position: absolute; left: 460px; top: 30px; width: 100px; }
</style>
</head>
<body>
<div class="canvas">

  <section class="panel panel--front">
    <svg class="brand-band" viewBox="0 0 617 222" aria-hidden="true">
      <polygon fill="#f4931f" points="0,4 60,0 140,3 230,1 330,4 430,0 520,3 617,1 617,218 540,222 440,219 330,222 220,219 120,222 40,219 0,222"/>
    </svg>
    <div class="mascot-art" role="img" aria-label="Illustration of the brand mascot animal standing"></div>
    <h1 class="brand-name">Badger<br>Bite</h1>
    <p class="slogan">Designed for strength,<br>built to last</p>
    <p class="product-line">8 Hole Sanding Discs</p>

    <div class="grit-row">
      <div class="grit"><div class="grit__count">20X</div>
        <svg width="96" height="96" viewBox="0 0 96 96"><circle cx="48" cy="48" r="48" fill="#f4931f"/><g fill="#fff"><circle cx="48" cy="20" r="4"/><circle cx="68" cy="28" r="4"/><circle cx="76" cy="48" r="4"/><circle cx="68" cy="68" r="4"/><circle cx="48" cy="76" r="4"/><circle cx="28" cy="68" r="4"/><circle cx="20" cy="48" r="4"/><circle cx="28" cy="28" r="4"/></g><text x="48" y="54" text-anchor="middle" fill="#fff" font-family="Oswald, sans-serif" font-weight="700" font-size="20">80</text><text x="48" y="63" text-anchor="middle" fill="#fff" font-family="Oswald, sans-serif" font-size="8">GRIP</text></svg></div>
      <div class="grit"><div class="grit__count">20X</div>
        <svg width="96" height="96" viewBox="0 0 96 96"><circle cx="48" cy="48" r="48" fill="#f4931f"/><g fill="#fff"><circle cx="48" cy="20" r="4"/><circle cx="68" cy="28" r="4"/><circle cx="76" cy="48" r="4"/><circle cx="68" cy="68" r="4"/><circle cx="48" cy="76" r="4"/><circle cx="28" cy="68" r="4"/><circle cx="20" cy="48" r="4"/><circle cx="28" cy="28" r="4"/></g><text x="48" y="54" text-anchor="middle" fill="#fff" font-family="Oswald, sans-serif" font-weight="700" font-size="20">80</text><text x="48" y="63" text-anchor="middle" fill="#fff" font-family="Oswald, sans-serif" font-size="8">GRIP</text></svg></div>
      <div class="grit"><div class="grit__count">20X</div>
        <svg width="96" height="96" viewBox="0 0 96 96"><circle cx="48" cy="48" r="48" fill="#f4931f"/><g fill="#fff"><circle cx="48" cy="20" r="4"/><circle cx="68" cy="28" r="4"/><circle cx="76" cy="48" r="4"/><circle cx="68" cy="68" r="4"/><circle cx="48" cy="76" r="4"/><circle cx="28" cy="68" r="4"/><circle cx="20" cy="48" r="4"/><circle cx="28" cy="28" r="4"/></g><text x="48" y="54" text-anchor="middle" fill="#fff" font-family="Oswald, sans-serif" font-weight="700" font-size="20">80</text><text x="48" y="63" text-anchor="middle" fill="#fff" font-family="Oswald, sans-serif" font-size="8">GRIP</text></svg></div>
      <div class="grit"><div class="grit__count"></div>
        <svg width="96" height="96" viewBox="0 0 96 96"><circle cx="48" cy="48" r="48" fill="#f4931f"/><g fill="#fff"><circle cx="48" cy="20" r="4"/><circle cx="68" cy="28" r="4"/><circle cx="76" cy="48" r="4"/><circle cx="68" cy="68" r="4"/><circle cx="48" cy="76" r="4"/><circle cx="28" cy="68" r="4"/><circle cx="20" cy="48" r="4"/><circle cx="28" cy="28" r="4"/></g><text x="48" y="56" text-anchor="middle" fill="#fff" font-family="Oswald, sans-serif" font-weight="700" font-size="20">5”</text></svg></div>
    </div>
  </section>

  <section class="panel panel--side">
    <p class="label vertical">8 Hole<br>Sanding<br>Discs</p>
    <div class="brand-name vertical">Badger<br>Bite</div>
    <div class="mascot-art" role="img" aria-label="Outline illustration of the brand mascot animal crouching"></div>
  </section>

  <section class="panel panel--bottom">
    <div class="mascot-art" role="img" aria-label="Outline illustration of the brand mascot animal standing"></div>
    <div class="brand-name">Badger<br>Bite</div>
    <p class="label">8 Hole<br>Sanding<br>Discs</p>
  </section>

</div>
</body>
</html>
```